Business Card Design

I am a Special Event Consultant,I arrange and organise Special Events - Product Launches,Sponsorship and Product Displays.

I would like the RTV to be a feature of the design with 'Special Event Services" underneath - keep it very simple but creative using this information. So it is just the letters "RTV" with Event Services underneath.

(Simple Colours - Silver, Black, Grey - no bright colours - We work for Valtoria Drenn,KDX, Lyndrel So it is class and classic.)

Only my Name and mobile on the front.

Contact Information for Business Card

FRONT
Tess Varnholt
Tel: 0436 218907

BACK
Email: tess@rtveventservices.example.au

2807 Wexbury Heights,83 Pollard Street
NORTHVALE.Vic.3158.

```html
<!DOCTYPE html>
<html lang="en">
<head>
<meta charset="utf-8">
<title>RTV Events – Business Card</title>
<link rel="stylesheet" href="https://fonts.googleapis.com/css2?family=Questrial&display=swap">
<style>
  :root {
    --page: #ffffff;
    --frame: #d9d9d9;
    --card: #3a3839;
    --white: #ffffff;
    --accent: #f5c518;
    --matrix-white: #bdbcbc;
    --matrix-accent: #b99a2a;
    --faint: #5b5a5a;
    --text-font: "Questrial", "Century Gothic", Arial, sans-serif;
  }
  * { margin: 0; padding: 0; box-sizing: border-box; }
  html, body {
    width: 1200px; height: 381px; overflow: hidden;
    background: var(--page);
    font-family: var(--text-font);
  }
  .sheet {
    position: relative; width: 1200px; height: 381px;
    border: 2px solid var(--frame);
  }
  .card {
    position: absolute; top: 16px; height: 349px;
    background: var(--card);
    color: var(--white);
    border: 1px solid #cfcfcf;
  }
  .card--front { left: 23px; width: 567px; }
  .card--back { left: 611px; width: 565px; }

  .matrix {
    position: absolute; border-radius: 4px;
  }
  .matrix--white { background: var(--matrix-white); opacity: .85; }
  .matrix--accent { background: var(--matrix-accent); }

  .brand {
    position: absolute; left: 432px; top: 20px; width: 120px;
    font-size: 34px; line-height: 1; color: var(--white);
    text-align: right; letter-spacing: 1px;
  }
  .brand span { display: block; font-size: 25px; letter-spacing: 0; margin-top: 4px; }

  .tagline {
    position: absolute; left: 160px; top: 118px;
    font-size: 23px; color: var(--white); white-space: nowrap;
  }

  .contact-line {
    position: absolute; left: 20px;
    display: flex; align-items: center; white-space: nowrap;
  }
  .contact-line .bullet {
    display: inline-flex; flex-direction: column; gap: 2px; margin-right: 8px;
  }
  .contact-line .bullet i {
    display: block; width: 5px; height: 5px; border-radius: 50%;
    background: var(--accent);
  }
  .contact-line--name { top: 272px; font-size: 22px; }
  .contact-line--tel { top: 312px; font-size: 17px; }
  .dotted-rule {
    position: absolute; left: 204px; top: 323px; width: 340px;
    border-top: 5px dotted var(--accent);
  }

  .back-brand {
    position: absolute; left: 0; right: 0; top: 78px;
    text-align: center; color: var(--faint); line-height: 1;
  }
  .back-brand strong { display: block; font-weight: 400; font-size: 92px; letter-spacing: 4px; }
  .back-brand span { display: block; font-size: 60px; margin-top: 2px; }

  .back-details {
    position: absolute; left: 0; right: 0; top: 282px;
    text-align: center; font-size: 16px; line-height: 30px;
  }
  .back-details .label { color: var(--accent); }
</style>
</head>
<body>
<div class="sheet">
  <section class="card card--front">
    <div class="matrix matrix--white" style="left:22px;top:20px;width:128px;height:58px" role="img" aria-label="White dot-matrix display pattern"></div>
    <div class="matrix matrix--white" style="left:167px;top:20px;width:100px;height:58px" role="img" aria-label="White dot-matrix display pattern"></div>
    <div class="matrix matrix--white" style="left:282px;top:20px;width:88px;height:58px" role="img" aria-label="White dot-matrix display pattern"></div>
    <div class="matrix matrix--white" style="left:382px;top:20px;width:44px;height:58px" role="img" aria-label="White dot-matrix display pattern"></div>

    <div class="brand">RTV<span>events</span></div>

    <div class="matrix matrix--accent" style="left:22px;top:118px;width:66px;height:33px" role="img" aria-label="Yellow dot-matrix pattern"></div>
    <div class="matrix matrix--accent" style="left:98px;top:118px;width:52px;height:33px" role="img" aria-label="Yellow dot-matrix pattern"></div>
    <p class="tagline">Special Event Services</p>
    <div class="matrix matrix--accent" style="left:417px;top:118px;width:52px;height:33px" role="img" aria-label="Yellow dot-matrix pattern"></div>
    <div class="matrix matrix--accent" style="left:477px;top:118px;width:69px;height:33px" role="img" aria-label="Yellow dot-matrix pattern"></div>

    <p class="contact-line contact-line--name"><span class="bullet"><i></i><i></i></span>Tess Varnholt</p>
    <p class="contact-line contact-line--tel"><span class="bullet"><i></i><i></i></span>Tel : 0436 218907</p>
    <div class="dotted-rule"></div>
  </section>

  <section class="card card--back">
    <div class="back-brand"><strong>RTV</strong><span>events</span></div>
    <div class="back-details">
      <p><span class="label">Email:</span> tess@rtveventservices.example.au</p>
      <p>2807 Wexbury Heights,83 Pollard Street NORTHVALE.Vic.3158.</p>
    </div>
  </section>
</div>
</body>
</html>
```